" VELTRIGRAFO, é uma empresa do grupo Dolvenca que atua a 19 anos no seguimento gráfico ( representante autorizado Pelnor) com serviços de manutençao, vendas, locaçao de equipamentos de impressao para todos os ramos de atividade. Com o tempo de mercado e experiência nas consultorias prestadas nas impresas conseguimos desenhar um modelo de gráfica rápida que será uma nova opçao para os empresários adquirirem através de franquia. A Veltrigrafo nascerá com o objetivo de multiplicar o modelo de negócio como franquia de gráfica rápida, se preocupando também com a sustentabilidade ambiental, procurando usar de maneira responsável os recursos, materiais, ferramentas e equipamentos disponíveis no mercado visando a preservaçao da floresta Amazônica e o meio ambiente. "

```html
<!DOCTYPE html>
<html lang="pt-BR">
<head>
<meta charset="utf-8">
<title>Veltrigrafo – Identidade Visual</title>
<link rel="stylesheet" href="https://fonts.googleapis.com/css2?family=Roboto+Condensed:wght@700&family=Roboto:wght@400;500&display=swap">
<style>
  :root {
    --bg: #d4d4d4;
    --paper: #ffffff;
    --green-deep: #1d5410;
    --green: #3a8a1c;
    --green-bright: #76bd3c;
    --green-pale: #dcefd0;
    --ink: #3b3b3b;
    --ink-soft: #7a7a7a;
  }
  * { box-sizing: border-box; margin: 0; padding: 0; }
  html, body { width: 1200px; height: 1200px; overflow: hidden; }
  body {
    background: var(--bg);
    font-family: "Roboto", Arial, sans-serif;
    color: var(--ink);
    position: relative;
  }
  .piece { position: absolute; background: var(--paper); overflow: hidden; }
  .piece svg.art { position: absolute; inset: 0; width: 100%; height: 100%; }

  .brand { position: absolute; display: flex; align-items: center; gap: 6px; }
  .brand .dot { border-radius: 50%; background: var(--green); flex: none; }
  .brand .name {
    font-family: "Roboto Condensed", "Arial Narrow", sans-serif;
    font-weight: 700; color: var(--green); letter-spacing: .02em; line-height: 1;
  }
  .brand.stack { flex-direction: column; gap: 5px; }

  .small { position: absolute; font-size: 7px; line-height: 1.45; color: var(--ink-soft); white-space: nowrap; }

  /* Folder */
  .folder { left: 108px; top: 252px; width: 480px; height: 348px; background: transparent; }
  .folder .cover { position: absolute; left: 0; top: 0; width: 252px; height: 348px;
    background: linear-gradient(135deg, var(--green-deep), var(--green) 55%, var(--green-deep)); overflow: hidden; }
  .folder .flap { position: absolute; left: 0; top: 0; width: 60px; height: 348px;
    background: linear-gradient(90deg, var(--green-bright), var(--green)); clip-path: polygon(0 8%, 100% 0, 100% 100%, 0 92%); }
  .folder .leaf-area { position: absolute; left: 70px; top: 40px; width: 170px; height: 190px; border-radius: 50%;
    background: radial-gradient(circle at 40% 40%, var(--green-bright), rgba(118,189,60,.2) 70%, transparent 72%); }
  .folder .pocket { position: absolute; left: 252px; top: 0; width: 228px; height: 348px; background: var(--paper); }
  .folder .pocket-edge { position: absolute; left: 252px; top: 0; width: 228px; height: 26px;
    background: linear-gradient(180deg, #eaeaea, var(--paper)); }
  .folder .contact { right: 14px; top: 318px; font-size: 6px; text-align: right; }

  /* Letterhead */
  .letterhead { left: 612px; top: 252px; width: 192px; height: 336px; }
  .watermark { position: absolute; left: 28px; top: 90px; width: 150px; height: 170px; border-radius: 50%;
    background: radial-gradient(circle at 45% 45%, var(--green-pale), rgba(220,239,208,0) 70%); }
  .letterhead .address { left: 0; width: 100%; top: 286px; font-size: 5.5px; text-align: center; }

  /* Cards */
  .card-front { left: 852px; top: 300px; width: 216px; height: 108px; }
  .card-back { left: 852px; top: 432px; width: 216px; height: 120px; }

  /* Screen */
  .screen { left: 132px; top: 648px; width: 360px; height: 240px; }

  /* Envelope */
  .envelope { left: 547px; top: 643px; width: 253px; height: 101px; }

  /* Tags */
  .tag { width: 113px; height: 259px; border-radius: 10px; top: 677px; }
  .tag-front { left: 835px; }
  .tag-back { left: 960px; }
  .tag .hole { position: absolute; left: 46px; top: 14px; width: 20px; height: 9px; border-radius: 5px; background: var(--bg); }
  .tag .person { position: absolute; left: 8px; top: 158px; font-size: 9px; color: #fff; line-height: 1.4; }
</style>
</head>
<body>

<!-- Folder -->
<section class="piece folder" aria-label="Pasta">
  <div class="cover">
    <div class="flap"></div>
    <div class="leaf-area" role="img" aria-label="Grande elemento decorativo em tons de verde"></div>
    <svg class="art" viewBox="0 0 252 348" aria-hidden="true">
      <path d="M60 300 C120 250 200 250 252 200" stroke="rgba(255,255,255,.5)" stroke-width="3" fill="none"/>
      <path d="M70 320 C130 270 200 270 252 225" stroke="rgba(255,255,255,.3)" stroke-width="2" fill="none"/>
    </svg>
  </div>
  <div class="pocket"></div>
  <div class="pocket-edge"></div>
  <div class="brand stack" style="left:332px; top:140px;">
    <span class="dot" style="width:22px;height:22px;"></span>
    <span class="name" style="font-size:14px;">VELTRIGRAFO</span>
  </div>
  <p class="small contact">contato@veltrigrafo.com.br<br>www.veltrigrafo.com.br</p>
</section>

<!-- Letterhead -->
<section class="piece letterhead" aria-label="Papel timbrado">
  <div class="brand" style="left:12px; top:12px;">
    <span class="dot" style="width:10px;height:10px;"></span>
    <span class="name" style="font-size:9px;">VELTRIGRAFO</span>
  </div>
  <p class="small" style="left:84px; top:10px; font-size:5.5px;">Tel. (92) 3020-4410<br>contato@veltrigrafo.com.br<br>www.veltrigrafo.com.br</p>
  <div class="watermark" role="img" aria-label="Elemento decorativo verde claro"></div>
  <svg class="art" viewBox="0 0 192 336" aria-hidden="true">
    <path d="M0 332 C60 316 130 320 192 302 L192 336 L0 336 Z" fill="var(--green)"/>
    <path d="M0 326 C60 310 130 314 192 296" stroke="var(--green-bright)" stroke-width="2" fill="none"/>
  </svg>
  <p class="small address">Rua das Palmeiras, 190 · Manaus · AM</p>
</section>

<!-- Business card front -->
<section class="piece card-front" aria-label="Cartão de visita, frente">
  <svg class="art" viewBox="0 0 216 108" aria-hidden="true">
    <path d="M140 0 L216 0 L216 108 L120 108 C160 80 150 30 140 0 Z" fill="var(--green)"/>
    <path d="M0 88 C60 80 110 96 216 70" stroke="var(--green-bright)" stroke-width="2" fill="none"/>
  </svg>
  <div class="brand" style="left:10px; top:10px;">
    <span class="dot" style="width:10px;height:10px;"></span>
    <span class="name" style="font-size:10px;">VELTRIGRAFO</span>
  </div>
  <p class="small" style="left:10px; top:32px; font-size:6px;">Nome Sobrenome<br>Cargo<br>Tel. (92) 3020-4410<br>contato@veltrigrafo.com.br<br>Rua das Palmeiras, 190</p>
</section>

<!-- Business card back -->
<section class="piece card-back" aria-label="Cartão de visita, verso">
  <svg class="art" viewBox="0 0 216 120" aria-hidden="true">
    <defs><linearGradient id="cardBack" x1="0" x2="1">
      <stop offset="0" stop-color="var(--green-deep)"/><stop offset="1" stop-color="var(--green-bright)"/>
    </linearGradient></defs>
    <rect width="216" height="120" fill="url(#cardBack)"/>
    <path d="M100 120 C130 70 216 60 216 60 L216 120 Z" fill="var(--paper)"/>
    <circle cx="55" cy="55" r="34" fill="none" stroke="rgba(255,255,255,.35)" stroke-width="2"/>
  </svg>
  <div class="brand" style="left:128px; top:88px;">
    <span class="dot" style="width:10px;height:10px;"></span>
    <span class="name" style="font-size:11px;">VELTRIGRAFO</span>
  </div>
</section>

<!-- Screen -->
<section class="piece screen" aria-label="Tela de apresentação">
  <svg class="art" viewBox="0 0 360 240" aria-hidden="true">
    <path d="M0 240 L0 190 C120 210 260 160 360 70 L360 240 Z" fill="var(--green)"/>
    <path d="M0 178 C120 198 260 150 360 58" stroke="var(--green-bright)" stroke-width="3" fill="none"/>
    <path d="M0 0 L150 0 C100 60 60 110 0 130 Z" fill="var(--green-pale)"/>
  </svg>
  <div class="brand stack" style="left:110px; top:60px;">
    <span class="dot" style="width:26px;height:26px;"></span>
    <span class="name" style="font-size:22px;">VELTRIGRAFO</span>
  </div>
  <p class="small" style="left:210px; top:200px; color:#fff;">contato@veltrigrafo.com.br<br>www.veltrigrafo.com.br</p>
</section>

<!-- Envelope -->
<section class="piece envelope" aria-label="Envelope">
  <svg class="art" viewBox="0 0 253 101" aria-hidden="true">
    <path d="M0 0 L253 0 L253 40 L126 60 L0 40 Z" fill="var(--green)"/>
    <path d="M0 40 L126 60 L253 40" stroke="var(--green-bright)" stroke-width="2" fill="none"/>
    <rect y="92" width="253" height="9" fill="var(--green)"/>
  </svg>
  <div class="brand stack" style="left:100px; top:22px;">
    <span class="dot" style="width:14px;height:14px; background:var(--paper);"></span>
    <span class="name" style="font-size:12px;">VELTRIGRAFO</span>
  </div>
</section>

<!-- Tag front -->
<section class="piece tag tag-front" aria-label="Crachá, frente">
  <svg class="art" viewBox="0 0 113 259" aria-hidden="true">
    <path d="M0 130 C40 110 80 120 113 100 L113 259 L0 259 Z" fill="var(--green)"/>
    <path d="M0 122 C40 102 80 112 113 92" stroke="var(--green-bright)" stroke-width="2" fill="none"/>
  </svg>
  <div class="hole"></div>
  <div class="brand" style="left:10px; top:40px;">
    <span class="dot" style="width:9px;height:9px;"></span>
    <span class="name" style="font-size:11px;">VELTRIGRAFO</span>
  </div>
  <p class="person">Nome Sobrenome<br>Cargo</p>
</section>

<!-- Tag back -->
<section class="piece tag tag-back" aria-label="Crachá, verso">
  <svg class="art" viewBox="0 0 113 259" aria-hidden="true">
    <path d="M0 200 C40 190 80 215 113 190 L113 259 L0 259 Z" fill="var(--green)"/>
  </svg>
  <div class="hole"></div>
  <p class="small" style="left:10px; top:44px; font-size:6px;">RG: 00.000.000-0<br>CPF: 000.000.000-00<br>Tel. (92) 3020-4410<br>contato@veltrigrafo.com.br</p>
  <div class="brand" style="left:54px; top:240px;">
    <span class="name" style="font-size:8px; color:#fff;">VELTRIGRAFO</span>
  </div>
</section>

</body>
</html>
```